Web Page for marketing online agency

We are an online marketing agency that is acing the direct response model. We engage with our customers throughout different marketing techniques as research copy-writing, advertisements and content writing. We would need a website design that will have four main aspects: The Vision; stating who we are, The Mission; stating what we do, The Team And It's Values, and a Contact Form. For this design we would want a sharp, clean and smart approach, with illustrated elements or suggestive images. You can use the attached copy, the logo, the USP and the motto. Please integrate them as you see fit while keeping in mind the previous needs and copy. This website is going to be our connection with our possible partners, future colleagues and even our clients. You may submit a design for one page or integrate the 4 different aspects on separate web pages.
Target Market(s)
business partners, future employees, age range 25-60
Industry/Entity Type
Direct Marketing
Number of Pages Required
1 page
Requirements
Must have
- Menu / Header
- 4 Parts or 4 Pages including: vision, mission, team, contact
- Logo
- Motto: Direct Brilliance
- USP: We help people help themselves.
- The copy attached
Nice to have
- Representative illustrated images or elements
Should not have
- A boring design, classical design - Pagequill like

```html
<!DOCTYPE html>
<html lang="en">
<head>
<meta charset="utf-8">
<title>Lumenway – Direct Brilliance</title>
<link href="https://fonts.googleapis.com/css2?family=Lato:wght@300;400;700;900&display=swap" rel="stylesheet">
<style>
:root{
  --blue:#2a8fd8;
  --ink:#333a40;
  --muted:#7a8288;
  --dark:#1f2326;
  --dark-2:#2b2f33;
  --white:#ffffff;
}
*{box-sizing:border-box;margin:0;padding:0}
html,body{width:1200px;height:3152px;overflow:hidden}
body{font-family:"Lato",Arial,sans-serif;color:var(--ink);background:var(--white);position:relative}
.site-header{position:absolute;top:0;left:0;width:1200px;height:84px;background:var(--white);display:flex;align-items:center;justify-content:space-between;padding:0 100px;z-index:3}
.brand{display:flex;align-items:center;gap:10px;font-weight:900;font-size:26px;color:var(--ink)}
.brand-dot{width:12px;height:12px;border-radius:50%;background:var(--blue)}
.main-nav{display:flex;gap:40px;font-size:12px;font-weight:700;letter-spacing:.5px}
.main-nav a{color:var(--ink);text-decoration:none;padding:6px 0}
.main-nav a.active{color:var(--blue);border-bottom:2px solid var(--blue)}
.btn{display:inline-block;padding:14px 38px;border-radius:30px;font-size:13px;font-weight:700;letter-spacing:.5px;text-decoration:none}
.btn-light{border:2px solid var(--white);color:var(--white)}
.btn-outline{border:2px solid var(--ink);color:var(--ink)}
.btn-blue-outline{border:2px solid var(--blue);color:var(--blue)}
.btn-solid{background:var(--blue);color:var(--white);padding:16px 48px}

.hero{position:absolute;top:84px;left:0;width:1200px;height:680px;background:linear-gradient(120deg,#55595d 0%,#8a8f94 40%,#4a4e52 100%)}
.hero-shade{position:absolute;inset:0;background:rgba(25,28,32,.35)}
.hero-copy{position:absolute;left:100px;top:150px;color:var(--white)}
.hero-copy h1{font-size:44px;font-weight:900;line-height:1.1;letter-spacing:1px}
.hero-copy p{font-size:30px;font-weight:400;margin:10px 0 40px}
.cut{position:absolute;left:0;width:1200px}

.who{position:absolute;top:770px;left:0;width:1200px;height:570px}
.who-art{position:absolute;left:96px;top:20px;width:300px;height:300px;border-radius:50%;background:radial-gradient(circle,#e8eef3 0%,#b9cfe0 60%,#5b8fbf 100%)}
.who-copy{position:absolute;left:540px;top:40px;width:560px}
.who-copy h2{font-size:40px;font-weight:900;margin-bottom:14px}
.lead{color:var(--blue);font-size:16px;line-height:1.5;margin-bottom:14px}
.body-text{color:var(--muted);font-size:13px;line-height:1.6;margin-bottom:34px}

.mission{position:absolute;top:1340px;left:0;width:1200px;height:470px;background:linear-gradient(110deg,#1f7fcc 0%,#3aa0e6 50%,#2484cf 100%);color:var(--white);text-align:center}
.mission h2{font-size:40px;font-weight:900;padding-top:70px}
.mission .tagline{font-size:32px;font-weight:300;opacity:.7;margin:8px 0 18px}
.mission .intro{font-size:16px;margin-bottom:10px}
.ticks{list-style:none;display:inline-block;text-align:left;font-size:14px;line-height:1.9}
.ticks li{display:flex;align-items:center;gap:10px}
.mission .btn{margin-top:24px}

.team{position:absolute;top:1810px;left:0;width:1200px;height:760px;text-align:center}
.team h2{font-size:40px;font-weight:900;padding-top:60px}
.team .intro{color:var(--muted);font-size:14px;line-height:1.6;width:780px;margin:14px auto 0}
.member{position:absolute;top:230px;width:400px;text-align:center}
.member-photo{width:130px;height:130px;border-radius:50%;margin:0 auto 18px;background:linear-gradient(135deg,#9aa1a7,#4c5257)}
.member h3{color:var(--blue);font-size:20px;font-weight:700}
.member .role{color:var(--muted);font-size:13px;margin:4px 0 14px}
.member .bio{color:var(--muted);font-size:12px;line-height:1.6;height:80px;margin-bottom:20px}

.contact{position:absolute;top:2570px;left:0;width:1200px;height:582px;background:var(--dark)}
.contact h2{color:var(--white);font-size:40px;font-weight:700;text-align:center;padding-top:150px}
.contact-form{position:absolute;left:100px;top:230px;width:1000px}
.field-row{display:flex;gap:20px;margin-bottom:20px}
.field{flex:1;height:44px;background:var(--dark-2);border:1px solid #3c4146;color:#8a9096;font-size:12px;padding:14px}
.field-area{height:100px}
.submit{text-align:center;margin-top:24px}
.footer-nav{position:absolute;left:0;top:505px;width:1200px;display:flex;justify-content:center;gap:34px;font-size:11px;color:#8a9096}
.copyright{position:absolute;left:0;top:540px;width:1200px;text-align:center;font-size:10px;color:#6b7176}
</style>
</head>
<body>
<header class="site-header">
  <div class="brand"><span>Lumenway</span><span class="brand-dot"></span></div>
  <nav class="main-nav">
    <a class="active" href="#">HOME</a><a href="#">WHO WE ARE</a><a href="#">OUR MISSION</a><a href="#">MARKETING</a><a href="#">OUR TEAM</a><a href="#">CONTACT US</a>
  </nav>
</header>

<section class="hero" role="img" aria-label="Dimmed photograph of a team working around a desk">
  <div class="hero-shade"></div>
  <div class="hero-copy">
    <h1>LUMENWAY - DIRECT<br>BRILLIANCE</h1>
    <p>We help people help themselves.</p>
    <a class="btn btn-light" href="#">LEARN MORE</a>
  </div>
  <svg class="cut" style="top:440px" width="1200" height="240" viewBox="0 0 1200 240"><polygon points="0,240 1200,0 1200,240" fill="#ffffff"/></svg>
</section>

<section class="who">
  <div class="who-art" role="img" aria-label="Illustration of business people at a table beneath a circle of marketing icons"></div>
  <div class="who-copy">
    <h2>WHO WE ARE?</h2>
    <p class="lead">We are a direct response company that creates and sells information products and services that millions of people find interesting and important in their lives.</p>
    <p class="body-text">We are specialised in the self reliance market and we serve people who crave more from life. We are in this business to aim at globally giving individuals what we know and help them become people who need safety, comfort and peace of mind.</p>
    <a class="btn btn-outline" href="#">LEARN MORE</a>
  </div>
</section>

<section class="mission" role="img" aria-label="Blue toned photograph of a city skyline">
  <h2>OUR MISSION</h2>
  <p class="tagline">We live and breathe direct response marketing.</p>
  <p class="intro">We are masters of direct response marketing. Our expertise is three folded:</p>
  <ul class="ticks">
    <li><svg width="14" height="14" viewBox="0 0 14 14"><circle cx="7" cy="7" r="7" fill="#fff"/><path d="M4 7l2 2 4-4" stroke="#2a8fd8" stroke-width="1.8" fill="none"/></svg>We create and aggregate great information products</li>
    <li><svg width="14" height="14" viewBox="0 0 14 14"><circle cx="7" cy="7" r="7" fill="#fff"/><path d="M4 7l2 2 4-4" stroke="#2a8fd8" stroke-width="1.8" fill="none"/></svg>We write content that compels people to act</li>
    <li><svg width="14" height="14" viewBox="0 0 14 14"><circle cx="7" cy="7" r="7" fill="#fff"/><path d="M4 7l2 2 4-4" stroke="#2a8fd8" stroke-width="1.8" fill="none"/></svg>We do deep research to offer simple quick and easy solutions to people's lasting problems.</li>
  </ul>
  <br>
  <a class="btn btn-light" href="#">LEARN MORE</a>
</section>

<section class="team">
  <h2>OUR TEAM</h2>
  <p class="intro">We're a small team of smart, funny, hard working specialists who are pushing to become the #1 company in self reliance. High ambition, radical honesty, and a result oriented mindset are encouraged at Lumenway.</p>
  <div class="member" style="left:140px">
    <div class="member-photo" role="img" aria-label="Portrait photo of the CEO"></div>
    <h3>Dorin Mira</h3>
    <p class="role">CEO Lumenway</p>
    <p class="bio">Dorin started in marketing at 21 and has since built campaigns for many brands. He leads our vision, trains our team, and believes every message must earn a reader's trust before asking for the sale.</p>
    <a class="btn btn-blue-outline" href="#">LEARN MORE</a>
  </div>
  <div class="member" style="left:660px">
    <div class="member-photo" role="img" aria-label="Portrait photo of the co-founder"></div>
    <h3>Andrei Lazar</h3>
    <p class="role">Co-Founder &amp; Media Manager Lumenway</p>
    <p class="bio">Since he was twenty, Andrei has run paid media across many offers. He loves clean data, smart testing and fast growth.</p>
    <a class="btn btn-blue-outline" href="#">LEARN MORE</a>
  </div>
</section>

<section class="contact">
  <svg class="cut" style="top:0" width="1200" height="100" viewBox="0 0 1200 100"><polygon points="0,0 1200,0 1200,100" fill="#ffffff"/></svg>
  <h2>CONTACT US</h2>
  <form class="contact-form">
    <div class="field-row">
      <div class="field">Full Name</div>
      <div class="field">E-mail address</div>
      <div class="field">Website</div>
    </div>
    <div class="field field-area">Message</div>
    <div class="submit"><span class="btn btn-solid">SUBMIT NOW!</span></div>
  </form>
  <nav class="footer-nav"><span>Home</span><span>Who We Are</span><span>Our Mission</span><span>Marketing</span><span>Our Team</span><span>Contact Us</span></nav>
  <p class="copyright">© 2016 Lumenway · All rights reserved · Privacy</p>
</section>
</body>
</html>
```